Drapery & Decor Atelier Project…
I am looking for a new website design for a store front “Drapery & Decor Atelier” business. Their customer would walk in off the street to have curtains designed for their home or business. This is not an ecommerce website.
The website colors should be light blue, dark blue, white and maybe tan. Be creative.
The curtains they sell can be found at www.plvexo.example and www.dombly.example. Please use images from these two website.
Navigation:
Home
Our Studio
Our Services
Our Manufactures
PLVEXO
Dombly
Our Process
Testimonials
Refer a Client
Subscribe to our Newsletter
Our Blog – (Needed for Internet Marketing)
Contact Us
The website should have a large footer for internet marketing purposes.
Updates
Great designs. Thank you everyone. I have sent them all to the client and i am waiting for feedback. I will let everyone know as soon as possible.
Sorry for the delay everyone. The client has been on vacation and has not provided feedback yet. As soon as I have an update I will let everyone know.

```html
<!DOCTYPE html>
<html lang="en">
<head>
<meta charset="utf-8">
<title>Drapery &amp; Decor Atelier</title>
<link rel="stylesheet" href="https://fonts.googleapis.com/css2?family=Arimo:wght@400;700&family=PT+Sans+Narrow:wght@700&display=swap">
<style>
:root{
  --black:#050505;
  --blue:#1f73c4;
  --blue-deep:#0d5cab;
  --blue-light:#3d9be6;
  --white:#ffffff;
  --page:#f3f3f3;
  --panel:#e3e3e3;
  --panel-line:#c4c4c4;
  --ink:#2b2b2b;
  --nav:#444444;
  --link:#1f6fbf;
  --footer:#3d3d3d;
  --footer-text:#9a9a9a;
}
*{margin:0;padding:0;box-sizing:border-box}
html,body{width:1041px;height:1200px;overflow:hidden;background:var(--page)}
body{font-family:"Arimo",Arial,sans-serif;color:var(--ink)}
.canvas{position:relative;width:1041px;height:1200px;overflow:hidden;background:var(--page)}
.abs{position:absolute}

.topbar{left:0;top:0;width:1041px;height:37px;background:var(--black)}
.search{left:748px;top:5px;width:214px;height:25px;background:var(--white);border-radius:3px;border:1px solid #ccc;font-size:12px;color:#888;padding:5px 9px}
.search svg{position:absolute;right:7px;top:6px}
.utility{left:0;top:37px;width:1041px;height:24px;background:var(--blue)}
.utility ul{position:absolute;right:79px;top:5px;list-style:none;display:flex;font-size:10.5px;color:var(--white)}
.utility li+li::before{content:"|";margin:0 8px}

.header{left:0;top:61px;width:1041px;height:82px;background:linear-gradient(#ffffff,#f0f0f0);border-bottom:1px solid #d8d8d8}
.logo{left:74px;top:12px;font-family:"PT Sans Narrow",sans-serif;font-size:31px;line-height:31px;color:#1e1e1e;letter-spacing:-.3px}
.nav{right:78px;top:32px;list-style:none;display:flex;font-size:12.5px;font-weight:700;color:var(--nav)}
.nav li+li::before{content:"|";font-weight:400;margin:0 13px;color:#333}
.nav .current span{border-bottom:3px solid var(--blue);padding-bottom:3px;color:#333}

.hero{left:0;top:143px;width:1041px;height:406px;background:radial-gradient(ellipse at 62% 30%,var(--blue-light),var(--blue) 55%,var(--blue-deep))}
.hero-frame{left:75px;top:32px;width:386px;height:333px;background:var(--white);padding:7px}
.hero-photo{width:100%;height:100%;background:linear-gradient(135deg,#ece8df 0%,#d9cdb6 45%,#a27b55 80%,#8a6442 100%)}
.hero-copy{left:521px;top:44px;width:450px;font-size:27px;line-height:31px;color:var(--white);letter-spacing:-.6px}
.hero-copy p+p{margin-top:19px}
.btn-read{left:522px;top:312px;width:113px;height:31px;border-radius:5px;background:linear-gradient(#8fd2f2,#3fa0dc);color:#0e2f4b;font-size:12.5px;font-weight:700;padding:8px 0 0 14px;box-shadow:0 1px 2px rgba(0,0,0,.3)}
.btn-read svg{position:absolute;right:12px;top:11px}

.pager{left:449px;top:535px;width:140px;height:33px;background:var(--page);border:1px solid #d2d2d2;border-radius:3px}
.pager svg{position:absolute;left:0;top:0}

.panel{left:75px;top:582px;width:887px;height:319px;background:var(--panel);border:1px solid var(--panel-line)}
.divider{top:14px;width:1px;height:292px;background:var(--panel-line)}
.panel h2{position:absolute;top:26px;font-family:"PT Sans Narrow",sans-serif;font-size:24px;color:#222;letter-spacing:-.4px}
.services-list{left:23px;top:87px;list-style:none;font-size:11px}
.services-list li{height:26px;padding-left:20px;position:relative}
.services-list svg{position:absolute;left:0;top:1px}
.testimonial{left:337px;top:86px;width:226px;font-size:11px;line-height:15.7px;text-align:justify}
.author{left:337px;top:241px;width:226px;text-align:right;font-size:12.5px;font-weight:700;color:var(--link)}
.blog{left:622px;top:86px;width:230px;font-size:11px;line-height:15.7px}
.blog h3{font-size:11px;font-weight:700;margin-bottom:7px}
.blog article+article{margin-top:18px}

.footer{left:0;top:930px;width:1041px;height:270px;background:var(--footer)}
.footer h4{position:absolute;top:25px;font-size:16px;font-weight:400;color:var(--white)}
.footer ul.links{position:absolute;top:60px;list-style:none;font-size:12px;color:var(--footer-text);line-height:20.8px}
.join-input{left:690px;top:56px;width:198px;height:27px;background:var(--white);border:1px solid #bbb}
.btn-sign{left:897px;top:56px;width:66px;height:27px;border-radius:5px;background:linear-gradient(#8fd2f2,#3fa0dc);color:#0e2f4b;font-size:12px;font-weight:700;text-align:center;padding-top:7px}
.badge{left:711px;top:104px;width:111px;height:123px;background:var(--white)}
.badge span{position:absolute;left:11px;top:8px;width:89px;height:89px;border-radius:50%;background:#6a5a9a}
.footer-nav{left:74px;top:236px;font-size:12.5px;color:var(--footer-text);display:flex;list-style:none}
.footer-nav li+li::before{content:"|";margin:0 7px}
.copyright{right:78px;top:238px;font-size:11px;color:var(--footer-text)}
</style>
</head>
<body>
<div class="canvas">

  <div class="abs topbar">
    <div class="abs search">Search
      <svg width="12" height="12" viewBox="0 0 12 12"><circle cx="7" cy="5" r="3.3" fill="none" stroke="#2a6fb8" stroke-width="1.5"/><line x1="4.6" y1="7.4" x2="1.5" y2="10.5" stroke="#2a6fb8" stroke-width="1.8"/></svg>
    </div>
  </div>

  <div class="abs utility">
    <ul>
      <li>Subscribe to our Newsletter</li><li>Blog</li><li>Testimonials</li><li>Contact Us</li>
    </ul>
  </div>

  <header class="abs header">
    <div class="abs logo">DRAPERY &amp;<br>DECOR ATELIER</div>
    <ul class="abs nav">
      <li class="current"><span>Home</span></li><li>Studio</li><li>Services</li><li>Manufactures</li><li>PLVEXO</li><li>Dombly</li><li>Our Process</li><li>Refer a Client</li>
    </ul>
  </header>

  <section class="abs hero">
    <div class="abs hero-frame">
      <div class="hero-photo" role="img" aria-label="Striped upholstered armchair on a wooden floor in a bright living room"></div>
    </div>
    <div class="abs hero-copy">
      <p>Search through our extensive product offerings and make your selections of fabrics, furniture, wallcoverings, trimings, carpets and drapery hardware.</p>
      <p>Create a favorites folder to save and share. Click here for the classic product search.</p>
    </div>
    <div class="abs btn-read">READ MORE
      <svg width="6" height="10" viewBox="0 0 6 10"><path d="M0 0L6 5L0 10Z" fill="#0e2f4b"/></svg>
    </div>
  </section>

  <div class="abs pager">
    <svg width="140" height="33" viewBox="0 0 140 33">
      <path d="M20 11L15 17L20 23" fill="none" stroke="#555" stroke-width="2"/>
      <path d="M131 11L136 17L131 23" fill="none" stroke="#555" stroke-width="2" transform="translate(-3 0)"/>
      <circle cx="44" cy="17" r="6" fill="#9a9a9a" stroke="#6c6c6c" stroke-width="2"/>
      <circle cx="44" cy="17" r="3" fill="#d0d0d0"/>
      <circle cx="62" cy="17" r="6" fill="#888"/>
      <circle cx="80" cy="17" r="6" fill="#888"/>
      <circle cx="98" cy="17" r="6" fill="#888"/>
    </svg>
  </div>

  <section class="abs panel">
    <div class="abs divider" style="left:306px"></div>
    <div class="abs divider" style="left:593px"></div>

    <h2 style="left:23px">SERVICES</h2>
    <ul class="abs services-list">
      <li><svg width="12" height="12" viewBox="0 0 12 12"><path d="M1 6L4.5 10L11 1.5" fill="none" stroke="#1f6fbf" stroke-width="2.2"/></svg>Lorem Ipsum is simply dummy text of the printing</li>
      <li><svg width="12" height="12" viewBox="0 0 12 12"><path d="M1 6L4.5 10L11 1.5" fill="none" stroke="#1f6fbf" stroke-width="2.2"/></svg>Lorem Ipsum is simply dummy text of the printing</li>
      <li><svg width="12" height="12" viewBox="0 0 12 12"><path d="M1 6L4.5 10L11 1.5" fill="none" stroke="#1f6fbf" stroke-width="2.2"/></svg>Lorem Ipsum is simply dummy text of the printing</li>
      <li><svg width="12" height="12" viewBox="0 0 12 12"><path d="M1 6L4.5 10L11 1.5" fill="none" stroke="#1f6fbf" stroke-width="2.2"/></svg>Lorem Ipsum is simply dummy text of the printing</li>
      <li><svg width="12" height="12" viewBox="0 0 12 12"><path d="M1 6L4.5 10L11 1.5" fill="none" stroke="#1f6fbf" stroke-width="2.2"/></svg>Lorem Ipsum is simply dummy text of the printing</li>
      <li><svg width="12" height="12" viewBox="0 0 12 12"><path d="M1 6L4.5 10L11 1.5" fill="none" stroke="#1f6fbf" stroke-width="2.2"/></svg>Lorem Ipsum is simply dummy text of the printing</li>
      <li><svg width="12" height="12" viewBox="0 0 12 12"><path d="M1 6L4.5 10L11 1.5" fill="none" stroke="#1f6fbf" stroke-width="2.2"/></svg>Lorem Ipsum is simply dummy text of the printing</li>
    </ul>

    <h2 style="left:337px">TESTIMONIALS</h2>
    <p class="abs testimonial">Lorem Ipsum is simply dummy text of the printing and typesetting industry. Lorem Ipsum has been the industry's standard dummy text ever since the 1500s, when an unknown printer took a galley of type and scrambled it to make a type specimen book. It has survived not only five centuries, but also the leap into electronic typesetting, of them remaining essentially unchanged. versions of Lorem Ipsum.</p>
    <p class="abs author">- Lorem Ipsum</p>

    <h2 style="left:622px">BLOG</h2>
    <div class="abs blog">
      <article><h3>Posted on 12-8-2012</h3><p>Lorem Ipsum is simply dummy text of the printing and typesetting industry. Lorem Ipsum has been the industry's standard dummy text ever since the 1500s, when an unknown printer</p></article>
      <article><h3>Posted on 12-8-2012</h3><p>Lorem Ipsum is simply dummy text of the printing and typesetting industry. Lorem Ipsum has been the industry's standard dummy text ever since the 1500s, when an unknown printer</p></article>
    </div>
  </section>

  <footer class="abs footer">
    <h4 style="left:74px">Menu Heading 1</h4>
    <ul class="links" style="left:75px"><li>Lorem Lipsum</li><li>Lorem Lipsum</li><li>Lorem Lipsum</li><li>Lorem Lipsum</li><li>Lorem Lipsum</li><li>Lorem Lipsum</li><li>Lorem Lipsum</li></ul>
    <h4 style="left:273px">Menu Heading 2</h4>
    <ul class="links" style="left:273px"><li>Lorem Lipsum</li><li>Lorem Lipsum</li><li>Lorem Lipsum</li><li>Lorem Lipsum</li><li>Lorem Lipsum</li><li>Lorem Lipsum</li><li>Lorem Lipsum</li></ul>
    <h4 style="left:490px">Menu Heading 3</h4>
    <ul class="links" style="left:490px"><li>Lorem Lipsum</li><li>Lorem Lipsum</li><li>Lorem Lipsum</li><li>Lorem Lipsum</li><li>Lorem Lipsum</li><li>Lorem Lipsum</li><li>Lorem Lipsum</li></ul>
    <h4 style="left:690px">Join Now</h4>
    <div class="abs join-input"></div>
    <div class="abs btn-sign">SIGN UP</div>
    <div class="abs badge" role="img" aria-label="Membership badge"><span></span></div>
    <ul class="abs footer-nav"><li>Home</li><li>Privacy Policy</li><li>Terms of Use</li><li>Contact</li></ul>
    <div class="abs copyright">© 2012. All Rights Reserved.</div>
  </footer>

</div>
</body>
</html>
```